Business Card for a finance professional

I need a business card design to introduce myself to a professional networking (mainly banks) and potential companies to hire and remember me. I would like to use black, grey, white and maybe gold/silver colors and maybe something with my initials(R L F P T). The final design should communicate seriousness, profissionalism and something innovative.

The basic informations in the card are: Name, e-mail, phone number and trabnet. (I'm thinking to put some directly short link to my trabnet account or maybe some app - non QR Code - to add my contacts to a phone directly.)

My name is Mariana Lopes Ferreira Pinto dos Reis (I prefer to use only 'Mariana Lopes' or 'Mariana Reis' but i'm open to other suggestions) and I have 26 years old (just if it helps to build based in my age).
Updates

Dear designers, I wish to thank your participation in this project! It was very difficult to choose one! Thank your for your work! Best regards and success. Mariana

Target Market(s)

Potential hires and big companies.

Industry/Entity Type

Finance

Requirements
Must have
• The informations required at the business card are:
Name: Mariana Lopes F. P. dos Reis
Email: mariana.lop.reis@quellomail.com
Phone: +55 61 8493 5710
TrabNet: http://br.trabnet-perfis.com/in/marianalr/
Nice to have
• Modern and innovative look.
I suggest to use the colors black, grey, white, gold and/or silver, but I'm open to other colors.
Should not have
• A message showing that I need to be hired. It's more to "know me and remember me" than "hire me please".

```html
<!DOCTYPE html>
<html lang="en">
<head>
<meta charset="UTF-8">
<title>R L F P T — Business Card</title>
<link href="https://fonts.googleapis.com/css2?family=Roboto+Condensed:wght@700&family=Oswald:wght@300&family=Jost:wght@300&display=swap" rel="stylesheet">
<style>
  :root {
    --page: #ffffff;
    --card-black: #000000;
    --band-dark: #262626;
    --band-mid: #3a3a3a;
    --silver-light: #f2f2f2;
    --silver-mid: #bdbdbd;
    --silver-dark: #8a8a8a;
    --accent-red: #c8102e;
    --text-white: #ffffff;
    --text-name: #d0d0d0;
    --text-contact: #a6a6a6;
    --rule-grey: #8c8c8c;
    --mark-grey: #4a4a4a;
    --back-rule: #5e5e5e;
  }
  * { margin: 0; padding: 0; box-sizing: border-box; }
  html, body {
    width: 1200px;
    height: 1200px;
    overflow: hidden;
    background: var(--page);
  }
  .canvas {
    position: relative;
    width: 1200px;
    height: 1200px;
  }
  .card {
    position: absolute;
    left: 329px;
    width: 546px;
    height: 300px;
    background: var(--card-black);
    overflow: hidden;
    box-shadow: 7px 8px 9px rgba(0, 0, 0, 0.35);
  }
  .card--front { top: 205px; }
  .card--back { top: 657px; height: 303px; }

  .front-art {
    position: absolute;
    inset: 0;
    width: 100%;
    height: 100%;
  }
  .monogram {
    position: absolute;
    font-family: "Roboto Condensed", "Arial Narrow", sans-serif;
    font-weight: 700;
    line-height: 1;
    white-space: pre;
  }
  .card--front .monogram {
    left: 24px;
    top: 40px;
    font-size: 64px;
    letter-spacing: 8px;
    color: var(--text-white);
  }
  .holder-name {
    position: absolute;
    left: 21px;
    top: 107px;
    font-family: "Oswald", "Arial Narrow", sans-serif;
    font-weight: 300;
    font-size: 22px;
    line-height: 1;
    color: var(--text-name);
    white-space: nowrap;
  }
  .contact {
    position: absolute;
    left: 148px;
    top: 206px;
    padding-left: 17px;
    border-left: 3px solid var(--rule-grey);
    font-family: "Jost", "Helvetica", sans-serif;
    font-weight: 300;
    font-size: 16.5px;
    line-height: 23px;
    color: var(--text-contact);
    list-style: none;
    white-space: nowrap;
  }
  .card--back .monogram {
    left: 0;
    right: 0;
    top: 94px;
    text-align: center;
    font-size: 62px;
    letter-spacing: 8px;
    color: var(--mark-grey);
  }
  .back-rule {
    position: absolute;
    left: 0;
    right: 0;
    top: 154px;
    height: 3px;
    background: var(--back-rule);
  }
</style>
</head>
<body>
<main class="canvas">
  <section class="card card--front" aria-label="Business card front">
    <svg class="front-art" viewBox="0 0 546 300" preserveAspectRatio="none" aria-hidden="true">
      <defs>
        <linearGradient id="silverBand" x1="0" y1="0" x2="1" y2="0">
          <stop offset="0" stop-color="var(--silver-dark)"/>
          <stop offset="0.55" stop-color="var(--silver-mid)"/>
          <stop offset="1" stop-color="var(--silver-light)"/>
        </linearGradient>
        <linearGradient id="darkBand" x1="0" y1="0" x2="0" y2="1">
          <stop offset="0" stop-color="var(--band-mid)"/>
          <stop offset="1" stop-color="var(--band-dark)"/>
        </linearGradient>
      </defs>
      <rect class="silver-band" x="0" y="0" width="546" height="99" fill="url(#silverBand)"/>
      <path class="dark-band" d="M0 99 H546 V160 C470 150 420 142 330 142 C220 142 120 146 0 150 Z" fill="url(#darkBand)"/>
      <path class="gloss-sweep" d="M300 99 H546 V140 C470 120 390 108 300 99 Z" fill="#ffffff" fill-opacity="0.06"/>
      <rect class="accent-line" x="0" y="97" width="546" height="3" fill="var(--accent-red)"/>
    </svg>
    <div class="monogram">R L F P T</div>
    <p class="holder-name">Mariana Lopes F. P. dos Reis</p>
    <ul class="contact">
      <li>Email: mariana.lop.reis@quellomail.com</li>
      <li>Phone: +55 61 8493 5710</li>
      <li>TrabNet: br.trabnet-perfis.com/in/marianalr/</li>
    </ul>
  </section>

  <section class="card card--back" aria-label="Business card back">
    <div class="monogram">R L F P T</div>
    <div class="back-rule"></div>
  </section>
</main>
</body>
</html>
```